Book Flyer

I want a flyer that we can use to promote this book to educators and to leaders....below is a sample flyer but I want something bold and creative and different from this....it can be completely different from what is attached. I want to be a WOW to increase sales. Please include pic of book and how folks can get a copy....I've given you a few pics but please be creative ....looking for a wow.

```html
<!DOCTYPE html>
<html lang="en">
<head>
<meta charset="utf-8">
<title>Purposeful Excellence – Book Flyer</title>
<link href="https://fonts.googleapis.com/css2?family=Roboto:wght@300;400;500;700;900&family=Roboto+Condensed:wght@300;400;700&display=swap" rel="stylesheet">
<style>
  :root{
    --page:#dcdddf;
    --black:#000000;
    --blue:#1a7ec3;
    --blue-deep:#1478bf;
    --orange:#f47f22;
    --brown:#6b4021;
    --white:#ffffff;
    --ink:#0b0f14;
    --red:#d8323a;
    --navy:#1d2a4d;
  }
  *{margin:0;padding:0;box-sizing:border-box}
  html,body{width:1200px;height:1200px;overflow:hidden;background:var(--page)}
  .flyer{
    position:absolute;left:210px;top:95px;width:780px;height:1010px;
    background:var(--black);overflow:hidden;
    box-shadow:6px 8px 14px rgba(0,0,0,.35);
    font-family:"Roboto",sans-serif;color:var(--white);
  }
  .flyer-shapes{position:absolute;inset:0}
  .title{position:absolute;left:58px;top:36px;width:420px;line-height:1}
  .title-main{display:block;font-weight:900;font-size:67px;color:var(--blue);letter-spacing:-1.4px}
  .title-sub{display:block;font-weight:300;font-size:70px;color:var(--orange);margin-top:-6px;letter-spacing:-0.5px}
  .intro{
    position:absolute;left:62px;top:170px;width:408px;
    font-family:"Roboto Condensed",sans-serif;font-weight:300;font-size:14.6px;line-height:18.4px;
    text-align:justify;color:#e8e8e8;
  }
  .strategies-heading{position:absolute;left:60px;top:289px;width:414px;text-align:center;color:var(--orange);font-weight:700}
  .strategies-heading .big{display:block;font-size:27px;line-height:32px}
  .strategies-heading .small{display:block;font-size:21px;font-weight:500;line-height:28px}
  .strategy-bar{position:absolute;left:34px;top:408px;width:9px;height:261px;
    background:linear-gradient(var(--brown) 0 50%,var(--black) 50% 100%)}
  .strategy{position:absolute;left:60px;width:320px;color:var(--ink)}
  .strategy h3{font-family:"Roboto Condensed",sans-serif;font-weight:700;font-size:29px;line-height:30px;color:var(--white);margin-bottom:6px}
  .strategy p{font-size:12.2px;line-height:15.3px;font-weight:300}
  .strategy cite{display:block;font-style:normal;font-weight:700;font-size:12.2px;line-height:15.3px}
  .strategy-equity{top:404px}
  .strategy-equity p{width:236px}
  .strategy-change{top:507px}
  .strategy-change p{width:226px}
  .strategy-communication{top:593px}
  .strategy-communication p{width:262px}
  .book{position:absolute;left:34px;top:689px;width:139px;height:193px;background:var(--white);
    box-shadow:4px 5px 8px rgba(0,0,0,.45);overflow:hidden}
  .book-art{height:86px;background:linear-gradient(160deg,#24345f,#1a2547 60%,#2c3f6d)}
  .book-band{height:50px;background:var(--red);text-align:center;padding-top:6px}
  .book-title{font-family:"Roboto Condensed",sans-serif;font-weight:700;font-size:21px;line-height:22px;color:var(--white);letter-spacing:-0.5px}
  .book-title-sub{font-family:"Roboto Condensed",sans-serif;font-size:10px;color:#f5d24a;line-height:12px;text-align:right;padding-right:14px}
  .book-tagline{font-size:3.6px;color:#333;padding:5px 6px 0;text-transform:uppercase}
  .book-author{font-family:"Roboto Condensed",sans-serif;font-size:14px;color:var(--navy);text-align:right;padding-right:10px;margin-top:12px}
  .book-foreword{font-size:3.6px;color:#555;text-align:right;padding-right:10px;text-transform:uppercase}
  .about{position:absolute;left:226px;top:742px;width:476px;color:var(--ink)}
  .about h2{font-weight:900;font-size:32px;line-height:38px;margin-bottom:2px}
  .about p{font-weight:500;font-size:15.2px;line-height:18.4px}
  .contact{position:absolute;left:0;top:909px;width:780px;height:101px;display:flex;align-items:center;justify-content:center;
    font-weight:500;font-size:28.5px;color:var(--blue)}
</style>
</head>
<body>
<main class="flyer">
  <svg class="flyer-shapes" width="780" height="1010" viewBox="0 0 780 1010">
    <defs>
      <radialGradient id="portraitTone" cx="0.62" cy="0.45" r="0.7">
        <stop offset="0" stop-color="#c9cde0"/>
        <stop offset="0.45" stop-color="#8e8fa6"/>
        <stop offset="1" stop-color="#000000"/>
      </radialGradient>
    </defs>
    <rect x="480" y="40" width="300" height="870" fill="url(#portraitTone)" role="img" aria-label="Portrait photo of the author smiling, in a light checked shirt and patterned red tie, arms crossed"/>
    <polygon points="343,645 780,817 780,909 0,909" fill="var(--blue-deep)"/>
    <polygon points="0,286 206,386 0,302" fill="var(--brown)"/>
    <polygon points="0,297 483,530 0,897" fill="var(--orange)"/>
  </svg>

  <h1 class="title"><span class="title-main">PURPOSEFUL</span><span class="title-sub">EXCELLENCE</span></h1>

  <p class="intro">Purposeful Excellence is a book written for all leaders. Dr. Marcus Hale speaks from real life experiences that are relatable and from the heart. His leadership steps have helped him develop into one of the most accomplished administrative leaders in the country. The three specific strategies outlined in this book will transform your leadership skills and help you stay on track to ensure success.</p>

  <h2 class="strategies-heading"><span class="big">3 Fundamental Strategies</span><span class="small">That Drive Leadership</span></h2>

  <div class="strategy-bar"></div>
  <section class="strategy strategy-equity">
    <h3>1. EQUITY</h3>
    <p>Fariness does not mean everyone gets the same. Fairness means everyone gets what they need.</p>
    <cite>-Ray Morden</cite>
  </section>
  <section class="strategy strategy-change">
    <h3>2. CHANGE</h3>
    <p>If you do not change direction, you may end up where you are heading.</p>
    <cite>-Lin Tao</cite>
  </section>
  <section class="strategy strategy-communication">
    <h3>3. COMMUNICATION</h3>
    <p>The single biggest problem in communication is the illusinon that is has taken place.</p>
    <cite>-Lin Tao</cite>
  </section>

  <div class="book">
    <div class="book-art" role="img" aria-label="Book cover artwork of rising arrows in red, white and blue"></div>
    <div class="book-band">
      <div class="book-title">PURPOSEFUL</div>
      <div class="book-title-sub">EXCELLENCE</div>
    </div>
    <div class="book-tagline">3 Fundamental Strategies That Drive Educational Leadership</div>
    <div class="book-author">M. Marcus Hale</div>
    <div class="book-foreword">Foreword by Ron Paley</div>
  </div>

  <section class="about">
    <h2>About Dr. Hale</h2>
    <p>Distinguished as a vibrant, visionary, and innovative leader who recognizes that humility is the most important trait a leader can possess. Dr. Hale uses his prior experiences in business, education, and nonprofit to assist organization leaders from all industries build internal leadership capacity, including strategy &amp; talent management and development to maximize organizational potential and success.</p>
  </section>

  <footer class="contact">For more info contact Us : info@thehalegroup.com</footer>
</main>
</body>
</html>
```